KORBALT

The business want a professional looking business card. We have a scetch we will add but want the extra upgrade, and would like more suggestions for variations of our business cards.

```html
<!DOCTYPE html>
<html lang="en">
<head>
<meta charset="utf-8">
<title>KORBALT Business Card</title>
<link href="https://fonts.googleapis.com/css2?family=Marcellus&family=Nunito+Sans:wght@400;600&display=swap" rel="stylesheet">
<style>
  :root {
    --backdrop: #e4e4e4;
    --paper: #ffffff;
    --ink: #1c1c1c;
    --gold: #c39a3a;
    --gold-dark: #7a5424;
    --gold-light: #f3df9a;
    --gold-mid: #b8893a;
  }
  * { box-sizing: border-box; margin: 0; padding: 0; }
  html, body {
    width: 1200px; height: 745px; overflow: hidden;
    background: var(--backdrop);
  }
  .sheet {
    position: relative; width: 1200px; height: 745px;
    display: flex; gap: 40px; align-items: center; justify-content: center;
  }
  .card {
    position: relative; width: 540px; height: 309px; overflow: hidden;
    box-shadow: 0 10px 30px rgba(0,0,0,0.12);
  }
  /* Back face */
  .card-back {
    background: linear-gradient(160deg, var(--gold-light) 0%, var(--gold-mid) 38%, var(--gold-dark) 62%, var(--gold-mid) 85%, #c8a25a 100%);
    display: flex; align-items: center; justify-content: center;
  }
  .back-brand {
    display: flex; align-items: center; gap: 14px;
    font-family: "Marcellus", serif; font-size: 46px; letter-spacing: 2px;
    color: var(--gold-light);
  }
  .back-brand .mark-dot {
    width: 22px; height: 22px; border-radius: 50%; background: var(--gold-light);
  }
  /* Front face */
  .card-front { background: var(--paper); }
  .front-heading {
    position: absolute; left: 42px; top: 58px;
    font-family: "Marcellus", serif; font-size: 30px; letter-spacing: 1px;
    color: var(--gold);
  }
  .role {
    position: absolute; left: 42px; top: 112px;
    font-family: "Nunito Sans", sans-serif; font-size: 25px; font-weight: 400;
    color: var(--ink);
  }
  .person {
    position: absolute; left: 46px; top: 146px;
    font-family: "Nunito Sans", sans-serif; font-size: 15px;
    color: var(--ink);
  }
  .contacts {
    position: absolute; left: 46px; bottom: 30px;
    list-style: none;
    font-family: "Nunito Sans", sans-serif; font-size: 15px; color: var(--ink);
  }
  .contacts li { display: flex; align-items: center; gap: 12px; height: 24px; }
  .contacts svg { width: 16px; height: 16px; flex: none; }
  .corner-accent {
    position: absolute; right: -70px; top: 80px;
    width: 190px; height: 190px; border-radius: 50%;
    background: linear-gradient(150deg, var(--gold-light), var(--gold) 55%, var(--gold-dark));
  }
</style>
</head>
<body>
<main class="sheet">
  <section class="card card-back" aria-label="Card back">
    <div class="back-brand"><span class="mark-dot"></span>KORBALT</div>
  </section>

  <section class="card card-front" aria-label="Card front">
    <h1 class="front-heading">KORBALT SOLVANG</h1>
    <p class="role">CEO &amp; Founder</p>
    <p class="person">Lars Henrik Solvang</p>
    <ul class="contacts">
      <li>
        <svg viewBox="0 0 16 16" aria-hidden="true"><rect x="4" y="1" width="8" height="14" rx="1.5" fill="none" stroke="#c39a3a" stroke-width="1.6"/><circle cx="8" cy="12.4" r="0.9" fill="#c39a3a"/></svg>
        004791234567
      </li>
      <li>
        <svg viewBox="0 0 16 16" aria-hidden="true"><rect x="1" y="3.5" width="14" height="9" fill="#c39a3a"/><path d="M1 3.5 L8 9 L15 3.5" fill="none" stroke="#fff" stroke-width="1"/></svg>
        korbalt.llc@mailbox.cm
      </li>
      <li>
        <svg viewBox="0 0 16 16" aria-hidden="true"><g fill="none" stroke="#c39a3a" stroke-width="1.1"><circle cx="8" cy="8" r="6.5"/><ellipse cx="8" cy="8" rx="3" ry="6.5"/><path d="M1.5 8h13M2.5 4.8h11M2.5 11.2h11"/></g></svg>
        www.korbalt.llc
      </li>
    </ul>
    <div class="corner-accent" aria-hidden="true"></div>
  </section>
</main>
</body>
</html>
```